Harbour Blokes - community/social/support group for men needs a flyer

We need a flyer for our community group for display in GP clinics and other community services offices. Please refer to our website for design ideas: www.harbourblokes.org.au. We need it to be clean and simple to read.

Target Market(s)

Men 18+

Font styles to use
Serif

Colors
00a990

```html
<!DOCTYPE html>
<html lang="en">
<head>
<meta charset="utf-8">
<title>Harbour Blokes Flyer</title>
<link href="https://fonts.googleapis.com/css2?family=Arimo:wght@400;700&family=Raleway:wght@300;500&display=swap" rel="stylesheet">
<style>
:root{
  --navy:#131a2b;
  --teal:#00a990;
  --grey-band:#e8e8e8;
  --ink:#1d1d1f;
  --page-bg:#f2f2f2;
  --white:#ffffff;
  --photo-green:#5f7a48;
}
*{margin:0;padding:0;box-sizing:border-box}
html,body{width:1200px;height:1000px;overflow:hidden;background:var(--page-bg)}
body{position:relative;font-family:"Arimo",Arial,sans-serif;color:var(--ink)}
.flyer{position:absolute;left:270px;top:17px;width:676px;height:955px;background:var(--white);box-shadow:0 6px 18px rgba(0,0,0,.18);overflow:hidden}
.hero{position:absolute;left:0;top:0;width:676px;height:315px}
.hero svg{position:absolute;left:0;top:0}
.brand-name{position:absolute;left:29px;top:87px;font-family:"Raleway",sans-serif;font-weight:500;font-size:20px;letter-spacing:.2px;color:var(--white);white-space:nowrap}
.tagline{position:absolute;left:32px;top:144px;font-family:"Raleway",sans-serif;font-weight:300;font-size:30px;line-height:34.5px;letter-spacing:1px;color:var(--white)}
.tagline span{display:block}
.tagline span:nth-child(2){padding-left:11px}
.tagline span:nth-child(3){padding-left:23px}
.tagline span:nth-child(4){padding-left:34px}
.about{position:absolute;left:0;top:315px;width:676px;height:168px;background:var(--grey-band);padding:19px 25px 0 28px}
.about h2{font-size:18px;font-weight:700;color:var(--teal);margin-bottom:7px}
.about p{font-size:13px;line-height:16.4px;text-align:justify}
.photo{position:absolute;left:34px;width:304px;height:122px}
.photo-park{top:505px;background:linear-gradient(160deg,#7b8a5a,#5a4a3a 70%,#3a3328)}
.photo-hall{top:637px;background:linear-gradient(180deg,#c9d6dc,#6d7275 55%,#4b4d52)}
.projects{position:absolute;left:370px;top:503px;width:280px}
.projects h3{font-size:15.5px;font-weight:700;line-height:19.5px;margin-bottom:16px}
.projects ul{list-style:none}
.projects li{font-size:13.5px;height:27.2px;display:flex;align-items:flex-start;padding-left:10px;white-space:nowrap}
.projects li svg{margin-right:6px;margin-top:1px;flex:none}
.projects .more{font-size:13.5px;margin-top:-4px}
.divider{position:absolute;left:32px;top:784px}
.cta{position:absolute;left:0;top:808px;width:676px;text-align:center;font-size:13.2px;line-height:17.5px}
.cta strong{font-weight:700}
.cta .fb{margin-top:6px}
.footer{position:absolute;left:0;top:881px;width:676px;height:64px;background:var(--navy);color:var(--white)}
.footer-strip{position:absolute;left:0;top:945px;width:676px;height:10px;background:var(--teal)}
.footer-brand{position:absolute;left:29px;top:38px;font-family:"Raleway",sans-serif;font-weight:500;font-size:9px;letter-spacing:.2px;white-space:nowrap}
.footer-rule{position:absolute;left:124px;top:9px;width:1px;height:48px;background:rgba(255,255,255,.5)}
.footer-address{position:absolute;left:133px;top:14px;font-size:10.5px;line-height:12.5px}
.footer-support{position:absolute;right:111px;top:20px;text-align:right;font-size:10.5px;line-height:12.5px}
.council-badge{position:absolute;left:572px;top:15px;width:73px;height:31px;background:linear-gradient(180deg,#3b8fc9,#2f8a55)}
</style>
</head>
<body>
<div class="flyer">
  <header class="hero">
    <svg width="676" height="315" viewBox="0 0 676 315">
      <defs>
        <linearGradient id="photoGrad" x1="0" y1="0" x2="1" y2="1">
          <stop offset="0" stop-color="#6f8a4e"/>
          <stop offset=".5" stop-color="#b57a65"/>
          <stop offset="1" stop-color="#8a5a4c"/>
        </linearGradient>
      </defs>
      <rect x="0" y="0" width="676" height="315" fill="var(--photo-green)"/>
      <rect role="img" aria-label="Photo of three smiling men with arms around each other outdoors" x="200" y="0" width="476" height="315" fill="url(#photoGrad)"/>
      <polygon points="0,0 212,0 296,315 0,315" fill="var(--navy)"/>
      <polygon points="0,193 0,315 32,315" fill="var(--teal)"/>
      <polygon points="646,0 676,0 676,60" fill="var(--teal)"/>
    </svg>
    <div class="brand-name">HARBOUR BLOKES</div>
    <div class="tagline"><span>SOCIAL.</span><span>SUPPORT.</span><span>MATESHIP.</span><span>COMMUNITY.</span></div>
  </header>

  <section class="about">
    <h2>ABOUT US</h2>
    <p><strong>Harbour Blokes Inc.</strong> is a community group that supports the positive activity, engagement and inclusion of men in Bayview’s Saltmarsh Ranges. Our aim is to reduce the number of men who are socially disadvantaged, marginalised or isolated to become productive, active members of the local community. We do this by providing opportunities for men (18 years+) to come together in open, non-judgemental, safe spaces and participate in a range of social activities that encourage new friendships, normalise help-seeking behaviours and link with local support services.</p>
  </section>

  <div class="photo photo-park" role="img" aria-label="Photo of dads and kids at a park playground"></div>
  <div class="photo photo-hall" role="img" aria-label="Photo of men seated in a hall listening to a guest speaker"></div>

  <section class="projects">
    <h3>We run a number of projects each year, which currently include:</h3>
    <ul>
      <li><svg width="14" height="13" viewBox="0 0 14 13"><path d="M1 1l5 5.5-5 5.5M7 1l5 5.5-5 5.5" fill="none" stroke="var(--teal)" stroke-width="2.4"/></svg>Dads and kids playgroup</li>
      <li><svg width="14" height="13" viewBox="0 0 14 13"><path d="M1 1l5 5.5-5 5.5M7 1l5 5.5-5 5.5" fill="none" stroke="var(--teal)" stroke-width="2.4"/></svg>Games Night</li>
      <li><svg width="14" height="13" viewBox="0 0 14 13"><path d="M1 1l5 5.5-5 5.5M7 1l5 5.5-5 5.5" fill="none" stroke="var(--teal)" stroke-width="2.4"/></svg>Yarning Circle (men’s discussion group)</li>
      <li><svg width="14" height="13" viewBox="0 0 14 13"><path d="M1 1l5 5.5-5 5.5M7 1l5 5.5-5 5.5" fill="none" stroke="var(--teal)" stroke-width="2.4"/></svg>GBTIQ+ social dinners</li>
      <li><svg width="14" height="13" viewBox="0 0 14 13"><path d="M1 1l5 5.5-5 5.5M7 1l5 5.5-5 5.5" fill="none" stroke="var(--teal)" stroke-width="2.4"/></svg>Shared Services working bee’s</li>
      <li><svg width="14" height="13" viewBox="0 0 14 13"><path d="M1 1l5 5.5-5 5.5M7 1l5 5.5-5 5.5" fill="none" stroke="var(--teal)" stroke-width="2.4"/></svg>Guest speakers</li>
      <li><svg width="14" height="13" viewBox="0 0 14 13"><path d="M1 1l5 5.5-5 5.5M7 1l5 5.5-5 5.5" fill="none" stroke="var(--teal)" stroke-width="2.4"/></svg>Annual men’s gathering</li>
    </ul>
    <p class="more">And more.</p>
  </section>

  <svg class="divider" width="608" height="16" viewBox="0 0 608 16">
    <line x1="0" y1="8" x2="608" y2="8" stroke="var(--teal)" stroke-width="1.5"/>
    <polygon points="252,3 356,3 362,8 356,13 252,13 246,8" fill="var(--teal)"/>
  </svg>

  <section class="cta">
    <p>For a list of our current activities and to find our how you can get involved, please visit us online at:<br><strong>www.harbourblokes.org.au</strong></p>
    <p class="fb">Or, join our Chatterbox page for our latest updates: <strong>www.chatterbox.com/harbourblokesAU/</strong></p>
  </section>

  <footer class="footer">
    <div class="footer-brand">HARBOUR BLOKES</div>
    <div class="footer-rule"></div>
    <div class="footer-address">Harbour Blokes Inc.<br>PO Box 2471<br>Bayview VIC 3190</div>
    <div class="footer-support">PROUDLY SUPPORTED BY<br>COASTLINE SHIRE COUNCIL</div>
    <div class="council-badge"></div>
  </footer>
  <div class="footer-strip"></div>
</div>
</body>
</html>
```